WWW.VELTRONA.IT BUSINNES CARD

WE NEED A BUSINESS CARD . I HAVE A COMPANY IN ITALY NR 1 IN HAIR MEDICAL CARE AN HAIR REPLECEMENT . IN CARD I NEED WRITE WEB ADDRESS, MAIL , ADDRESS, TELEPHONE NUMBER , AND NAME
IN THE BACK SIDE I NEED MY DOCTOR LOGO .
MY WEB SITE IS WWW.VELTRONA.IT
Updates

Target Market(s)

CONSUMER B2C

Industry/Entity Type

Hair And Beauty

Contact Information for Business Card

I WANT A MEDICAL BUSINESS CARD.

Font styles to use
Other font styles liked:
• VERDANA

Colors
33a6d7
3176b5
85abd2
aedbee
eaf1f7
ffffff

Requirements
Must have
• I NEED MY LOGO AND LOGO OF DR VELTRONA

```html
<!DOCTYPE html>
<html lang="it">
<head>
<meta charset="utf-8">
<title>Veltrona – Business Card</title>
<link rel="stylesheet" href="https://fonts.googleapis.com/css2?family=Noto+Sans:ital,wght@0,400;0,700;1,700&display=swap">
<style>
  :root {
    --card-blue: #40a8d0;
    --card-blue-light: #4cb0d8;
    --card-blue-deep: #3a9fca;
    --white: #ffffff;
    --page: #ffffff;
    --mascot-top: #9fc9de;
    --mascot-mid: #e6f1f7;
    --mascot-bottom: #f0c2aa;
  }
  * { margin: 0; padding: 0; box-sizing: border-box; }
  html, body {
    width: 980px; height: 1200px; overflow: hidden;
    background: var(--page);
    font-family: "Noto Sans", Verdana, sans-serif;
    color: var(--white);
  }
  .canvas { position: relative; width: 980px; height: 1200px; }
  .card {
    position: absolute; left: 199px; width: 592px; height: 383px;
    background: linear-gradient(180deg, var(--card-blue-light) 0%, var(--card-blue) 50%, var(--card-blue-deep) 100%);
    overflow: hidden;
  }
  .card--front { top: 170px; }
  .card--back { top: 659px; }
  .card svg.frame { position: absolute; left: 0; top: 0; }
  .brand {
    position: absolute; left: 0; width: 100%; top: 54px;
    text-align: center; font-weight: 700; font-size: 54px; line-height: 1;
    letter-spacing: -0.5px;
  }
  .tagline {
    position: absolute; left: 0; width: 100%; top: 122px;
    text-align: center; font-size: 14px; letter-spacing: 0.2px;
  }
  .holder {
    position: absolute; left: 0; width: 100%; top: 178px;
    text-align: center; font-weight: 700; font-size: 23px; letter-spacing: 0.5px;
  }
  .address, .contacts {
    position: absolute; left: 0; width: 100%;
    text-align: center; font-size: 18px; letter-spacing: 0.6px;
    display: flex; justify-content: center; align-items: center; gap: 6px;
  }
  .address { top: 240px; }
  .contacts { top: 272px; gap: 22px; }
  .contacts span { display: inline-flex; align-items: center; gap: 6px; }
  .phone-number { font-weight: 700; }
  .icon { width: 16px; height: 16px; }
  .question {
    position: absolute; left: 76px; top: 145px;
    font-size: 21px; line-height: 33px; letter-spacing: 0.6px;
  }
  .doctor-name {
    position: absolute; left: 76px; top: 218px;
    font-size: 37px; font-weight: 700; font-style: italic; letter-spacing: 0.5px;
  }
  .website {
    position: absolute; left: 97px; top: 311px;
    font-size: 19px; font-weight: 700; letter-spacing: 0.6px;
  }
  .mascot-area {
    position: absolute; left: 452px; top: 26px; width: 118px; height: 330px;
    background: linear-gradient(180deg, var(--mascot-top) 0%, var(--mascot-mid) 60%, var(--mascot-bottom) 100%);
    border-radius: 24px;
    opacity: 0.85;
  }
</style>
</head>
<body>
<main class="canvas">

  <section class="card card--front" aria-label="Fronte biglietto">
    <svg class="frame" width="592" height="383" viewBox="0 0 592 383" aria-hidden="true">
      <g fill="none" stroke="#ffffff" stroke-width="2.2" stroke-linecap="round">
        <path d="M143 79 H55 V333 H455"/>
        <path d="M456 83 H535 V300"/>
      </g>
      <path d="M455 330 C470 327 478 325 483 327 C487 330 485 335 478 336 C470 337 462 336 455 336 Z" fill="#ffffff"/>
      <rect x="514" y="307" width="42" height="42" rx="6" fill="#ffffff"/>
    </svg>

    <div class="brand">Veltrona</div>
    <div class="tagline">CURA E REINTEGRAZIONE DEI CAPELLI</div>
    <div class="holder">Dr. veltrona</div>

    <div class="address">
      <svg class="icon" viewBox="0 0 16 16" aria-hidden="true"><path d="M8 1.5a4.5 4.5 0 0 0-4.5 4.5C3.5 9.5 8 14.5 8 14.5S12.5 9.5 12.5 6A4.5 4.5 0 0 0 8 1.5z" fill="none" stroke="#fff" stroke-width="1.2"/><circle cx="8" cy="6" r="1.6" fill="none" stroke="#fff" stroke-width="1.2"/></svg>
      Via del Lago 14, Verona, Italy
    </div>

    <div class="contacts">
      <span>
        <svg class="icon" viewBox="0 0 16 16" aria-hidden="true"><path d="M2 6.5 8 2l6 4.5V14H2z M2 6.5 8 10.5l6-4" fill="none" stroke="#fff" stroke-width="1.2" stroke-linejoin="round"/></svg>
        info@veltrona.it
      </span>
      <span>
        <svg class="icon" viewBox="0 0 16 16" aria-hidden="true"><path d="M4 1.8 6 4.5 4.8 6.2c.9 2 2.6 3.8 4.8 4.9L11.3 9.8 14 11.8 12.5 14C7 13.6 2.4 9 2 3.4z" fill="none" stroke="#fff" stroke-width="1.2" stroke-linejoin="round"/></svg>
        <b class="phone-number">+39045123487</b>
      </span>
    </div>
  </section>

  <section class="card card--back" aria-label="Retro biglietto">
    <svg class="frame" width="592" height="383" viewBox="0 0 592 383" aria-hidden="true">
      <path d="M440 81 H55 V305" fill="none" stroke="#ffffff" stroke-width="2.2" stroke-linecap="round"/>
      <rect x="34" y="304" width="42" height="42" rx="6" fill="#ffffff"/>
      <circle cx="342" cy="135" r="30" fill="#ffffff"/>
      <path d="M318 150 L292 165 L326 158 Z" fill="#ffffff"/>
      <text x="342" y="149" text-anchor="middle" font-family="Noto Sans, Verdana, sans-serif" font-weight="700" font-size="40" fill="#40a8d0">?</text>
    </svg>

    <p class="question">Hai una domanda?<br>Chiedi consiglio a</p>
    <p class="doctor-name">Dr. Veltrona</p>
    <p class="website">www.veltrona.it</p>

    <div class="mascot-area" role="img" aria-label="Mascotte del dottore: un capello in camice bianco con pollice alzato, in piedi su una pedana"></div>
  </section>

</main>
</body>
</html>
```